Bright Stride Clinic helping older adults use exercise as medicine

We need a website for a start up company providing exercise physiology and physiotherapy clinical services for people with serious health conditions such as cancer, diabetes and many others This is an exculsive service with limited time. The 2 main objectives of the website are to create leads for appointments and provide education about the benefits of exercise ie stretches, strength training, cardio vascular improvement for people with health conditions.
Please not too medical in design more fitness and lifestyle... sell the promise, please sell happy fit active people.

Target Market(s)

40-70 year old adults both male and female interested in a healthy lifestyle, ie baby boomers moderate education level (finished high school minimum) rural/country people

Industry/Entity Type

Health

Number of Pages Required

4 page

Font styles to use
Serif
Sans Serif

Colors
f26f22
3176b5

Requirements
Must have
• Website must have a blog/education area and a members area with access to an exercise database (picture, description and video)

```html
<!DOCTYPE html>
<html lang="en">
<head>
<meta charset="utf-8">
<title>Bright Stride Clinic</title>
<link href="https://fonts.googleapis.com/css2?family=Lato:wght@400;700&family=Roboto:wght@400;500&family=Courgette&display=swap" rel="stylesheet">
<style>
:root{
  --orange:#d86f1f;
  --orange-deep:#d05a0c;
  --orange-light:#efbd8f;
  --blue:#2e74b5;
  --navy:#12387f;
  --ink:#222;
  --grey:#555;
  --panel:#f3f3f3;
  --map-tone:#e6e0cf;
  --white:#fff;
}
*{margin:0;padding:0;box-sizing:border-box}
html,body{width:991px;height:1200px;overflow:hidden;background:var(--white)}
body{position:relative;font-family:"Roboto",Arial,sans-serif;color:var(--ink)}
.abs{position:absolute}

/* header */
.header-band{left:335px;top:0;width:656px;height:97px;background:var(--orange);border-bottom-left-radius:70px}
.brand{left:112px;top:40px;display:flex;align-items:center;gap:8px;font:700 30px "Lato",sans-serif;color:var(--blue)}
.brand-dot{width:22px;height:22px;border-radius:50%;background:var(--orange)}
.member-login{left:784px;top:5px;width:99px;height:19px;background:var(--blue);color:var(--white);font:400 11px "Lato",sans-serif;text-align:center;line-height:19px}
.top-contact{top:37px;display:flex;align-items:center;gap:6px;color:var(--white);font:400 13px "Lato",sans-serif}
.top-contact.phone{left:602px;font-size:14px}
.top-contact.mail{left:730px;font-size:12px}
.nav-item{top:68px;font:400 15px "Lato",sans-serif;color:var(--white)}
.nav-item.active{font-weight:700}

/* hero */
.hero{left:0;top:97px;width:991px;height:287px;background:linear-gradient(180deg,#d9cfc4 0%,#c9bfb6 45%,#9ea3a8 70%,#6f6b68 100%)}
.hero-title{left:603px;top:136px;width:260px;font:400 24px/30px "Courgette",cursive;color:#2a2a2a}
.slider-dots{left:688px;top:327px;display:flex;gap:8px}
.slider-dots span{width:11px;height:11px;background:#2c2c2c}
.slider-dots span:first-child{background:var(--orange)}

/* features */
.feature-card{left:108px;top:356px;width:774px;height:90px;background:var(--white);box-shadow:0 -2px 6px rgba(0,0,0,.15);border-radius:4px 4px 0 0}
.feature{top:380px;display:flex;align-items:center;gap:22px}
.feature-icon{width:62px;height:58px}
.feature-label{font:700 14px/16px "Lato",sans-serif;color:var(--orange)}

/* main content */
.section-title{font:700 20px "Lato",sans-serif;color:var(--blue)}
.section-title em{font-style:normal;color:var(--orange)}
.dotted{border-top:1px dotted #999;height:0}
.intro{left:135px;top:502px;width:470px;font-size:12.2px;line-height:20px;letter-spacing:-.1px;color:var(--ink)}
.intro b{font-weight:500}
.benefit{top:616px;width:160px;text-align:center}
.benefit h3{font:400 14px "Roboto",sans-serif;margin-bottom:10px}
.benefit-photo{width:96px;height:96px;margin:0 auto;border-radius:50%;border:2px solid #ccc;background:linear-gradient(180deg,#e3c9b2 0%,#caa388 50%,#3a3a3a 100%)}
.benefit p{font-size:11px;line-height:14px;margin-top:12px;color:#333}
.col-divider{width:0;border-left:1px dotted #aaa}

/* sidebar */
.side-box{left:639px;width:219px;background:var(--panel);border:1px solid #ddd;border-radius:4px}
.side-title{font:400 19px "Lato",sans-serif;color:var(--grey)}
.map-block{background:var(--map-tone)}
.contact-row{left:651px;display:flex;gap:14px;font-size:11px;line-height:14px;color:#333}
.contact-row svg{flex:none}
.hours-row{left:651px;font:400 11.5px "Roboto",sans-serif;color:#333}
.hours-row b{font:700 13px "Lato",sans-serif;color:var(--blue)}

/* blog */
.blog-arrow{width:15px;height:15px;border-radius:50%;border:1px solid #555}
.avatar{width:63px;height:63px;border-radius:50%;border:2px solid #ccc;background:linear-gradient(160deg,#e9d3b8,#b88d6c)}
.blog-author{font:400 12px "Lato",sans-serif;color:var(--navy)}
.blog-head{display:flex;justify-content:space-between;width:252px;font:500 12.5px "Roboto",sans-serif}
.blog-text{width:262px;font-size:11.2px;line-height:19px;color:#333}

/* footer */
.footer-shape{left:0;top:890px;width:991px;height:310px}
.foot-title{top:1030px;font:700 14px "Lato",sans-serif;color:var(--white)}
.foot-rule{border-top:1px dotted rgba(255,255,255,.8);height:0}
.foot-divider{top:1050px;width:0;height:120px;border-left:1px solid rgba(255,255,255,.35)}
.quick-links{left:110px;top:1061px;list-style:none;font:400 11.5px/13px "Lato",sans-serif;color:var(--white)}
.quick-links li{position:relative;padding-left:17px;margin-bottom:9px;width:120px}
.quick-links li::before{content:"»";position:absolute;left:0}
.foot-contact{left:271px;display:flex;gap:10px;font:400 11.5px/14px "Lato",sans-serif;color:var(--white)}
.foot-contact.strong{font-weight:700}
.foot-map{left:446px;top:1062px;width:169px;height:89px;border:2px solid var(--navy);background:var(--map-tone)}
.newsletter-copy{left:679px;top:1058px;width:200px;font:400 11px/14px "Lato",sans-serif;color:var(--white)}
.email-field{left:678px;top:1092px;width:134px;height:27px;background:var(--white);font:400 12px/27px "Lato",sans-serif;color:#333;padding-left:8px;border-radius:3px 0 0 3px}
.subscribe{left:812px;top:1092px;width:69px;height:27px;background:var(--navy);color:var(--white);font:700 11px/27px "Lato",sans-serif;text-align:center;border-radius:0 3px 3px 0}
.follow{left:678px;top:1133px;font:400 13px "Lato",sans-serif;color:var(--white)}
.social{top:1127px;width:25px;height:25px;border-radius:4px}
.copyright{left:0;top:1179px;width:991px;text-align:center;font:400 10.5px "Roboto",sans-serif;color:var(--white)}
</style>
</head>
<body>

<!-- Header -->
<div class="abs header-band"></div>
<div class="abs brand"><span class="brand-dot"></span>Bright Stride</div>
<div class="abs member-login">Member Login</div>
<div class="abs top-contact phone">
  <svg width="20" height="20" viewBox="0 0 20 20"><circle cx="10" cy="10" r="9" fill="none" stroke="#fff" stroke-width="1.5"/><path d="M7 5l2 2-1 2 3 3 2-1 2 2-2 2c-4 0-8-4-8-8z" fill="#fff"/></svg>
  123-456-7890
</div>
<div class="abs top-contact mail">
  <svg width="16" height="11" viewBox="0 0 16 11"><rect x=".5" y=".5" width="15" height="10" fill="none" stroke="#fff"/><path d="M.5 .5l7.5 6 7.5-6" fill="none" stroke="#fff"/></svg>
  info@brightstride.com
</div>
<nav>
  <span class="abs nav-item active" style="left:445px">Home</span>
  <span class="abs nav-item" style="left:502px">Accredited Exercise Physiologist</span>
  <span class="abs nav-item" style="left:734px">Services</span>
  <span class="abs nav-item" style="left:810px">Contact Us</span>
</nav>

<!-- Hero -->
<div class="abs hero" role="img" aria-label="Photo of an older couple walking hand in hand along a beach at sunset"></div>
<div class="abs hero-title">Lorem ipsereum dolor sit amet, consectetuer adipiscing elit</div>
<div class="abs slider-dots"><span></span><span></span><span></span><span></span></div>

<!-- Feature links -->
<div class="abs feature-card"></div>
<div class="abs feature" style="left:130px">
  <svg class="feature-icon" viewBox="0 0 62 58"><path d="M6 50a25 25 0 0 1 50 0" fill="none" stroke="#d86f1f" stroke-width="3"/><rect x="16" y="26" width="30" height="26" rx="2" fill="#2e74b5"/><g fill="#fff"><rect x="19" y="34" width="5" height="4"/><rect x="26" y="34" width="5" height="4"/><rect x="33" y="34" width="5" height="4"/><rect x="40" y="34" width="4" height="4"/><rect x="19" y="41" width="5" height="4"/><rect x="26" y="41" width="5" height="4"/><rect x="33" y="41" width="5" height="4"/><rect x="40" y="41" width="4" height="4"/></g></svg>
  <span class="feature-label">REQUEST AN<br>APPOINTMENT</span>
</div>
<div class="abs feature" style="left:384px">
  <svg class="feature-icon" viewBox="0 0 62 58"><path d="M6 50a25 25 0 0 1 50 0" fill="none" stroke="#d86f1f" stroke-width="3"/><circle cx="27" cy="30" r="6" fill="#2e74b5"/><path d="M17 56v-8c0-6 4-10 10-10s10 4 10 10v8z" fill="#2e74b5"/><path d="M38 24h4v-4h4v4h4v4h-4v4h-4v-4h-4z" fill="#2e74b5"/></svg>
  <span class="feature-label">MEET THE<br>PHYSIOLOGIST</span>
</div>
<div class="abs feature" style="left:630px">
  <svg class="feature-icon" viewBox="0 0 62 58"><path d="M6 50a25 25 0 0 1 50 0" fill="none" stroke="#d86f1f" stroke-width="3"/><rect x="18" y="28" width="24" height="22" rx="3" fill="none" stroke="#2e74b5" stroke-width="3"/><path d="M22 38l7 7 16-18" fill="none" stroke="#2e74b5" stroke-width="4"/></svg>
  <span class="feature-label" style="margin-left:-4px">ACCREDITED EXERCISE<br>PHYSIOLOGIST</span>
</div>

<!-- Welcome -->
<h1 class="abs section-title" style="left:135px;top:463px">Welcome To <em>Bright Stride</em></h1>
<div class="abs dotted" style="left:135px;top:493px;width:465px"></div>
<p class="abs intro">Lorem ipsum dolor sit amet, consectetuer adipiscing elit, sed diam nonummy niererebh euismod tincidunt ut laoreet dolore magna aliquam erat volutpat. Ut wisi enim ad ererw minim veniam, quis nostrud<b>.....read more</b></p>

<!-- Benefits -->
<h2 class="abs section-title" style="left:135px;top:576px">Benefits of <em>Exercises</em></h2>
<div class="abs dotted" style="left:135px;top:606px;width:465px"></div>
<div class="abs benefit" style="left:116px"><h3>Stretches</h3><div class="benefit-photo" role="img" aria-label="Photo of a woman doing a shoulder stretch"></div><p>Lorem ipsum dolor sit<br>ametii consectet.</p></div>
<div class="abs col-divider" style="left:270px;top:617px;height:160px"></div>
<div class="abs benefit" style="left:277px"><h3>Strength Training</h3><div class="benefit-photo" role="img" aria-label="Photo of a woman doing an arm strength exercise"></div><p>Lorem ipsum dolor sit<br>ametii consectet.</p></div>
<div class="abs col-divider" style="left:438px;top:617px;height:160px"></div>
<div class="abs benefit" style="left:450px"><h3>Cardio Improvement</h3><div class="benefit-photo" role="img" aria-label="Photo of a woman stretching her arms overhead"></div><p>Lorem ipsum dolor sit<br>ametii consectet.</p></div>

<!-- Sidebar contact -->
<div class="abs side-box" style="top:462px;height:224px"></div>
<h2 class="abs side-title" style="left:648px;top:464px">Contact Us</h2>
<div class="abs dotted" style="left:648px;top:494px;width:203px"></div>
<div class="abs map-block" style="left:647px;top:504px;width:203px;height:93px" role="img" aria-label="Street map showing the clinic location"></div>
<div class="abs" style="left:767px;top:564px;width:82px;height:32px;background:#fff;border-radius:6px;font-size:11px;line-height:13px;text-align:center;padding-top:4px;color:#222">Click on map<br>to expand</div>
<div class="abs contact-row" style="top:606px">
  <svg width="14" height="18" viewBox="0 0 14 18"><path d="M7 0a7 7 0 0 1 7 7c0 5-7 11-7 11S0 12 0 7a7 7 0 0 1 7-7z" fill="#d86f1f"/><circle cx="7" cy="7" r="2.5" fill="#fff"/></svg>
  <span>Street Name, City Name, State,<br>Pin Code</span>
</div>
<div class="abs contact-row" style="top:641px;align-items:center">
  <svg width="16" height="16" viewBox="0 0 20 20"><circle cx="10" cy="10" r="9" fill="none" stroke="#d86f1f" stroke-width="1.8"/><path d="M7 5l2 2-1 2 3 3 2-1 2 2-2 2c-4 0-8-4-8-8z" fill="#d86f1f"/></svg>
  <span>123-456-7890</span>
</div>
<div class="abs contact-row" style="top:666px;align-items:center">
  <svg width="16" height="12" viewBox="0 0 16 12"><rect x="0" y="2" width="16" height="10" fill="#d86f1f"/><path d="M0 2l8 6 8-6" fill="none" stroke="#fff"/></svg>
  <span>info@brightstride.com</span>
</div>

<!-- Hours -->
<div class="abs side-box" style="top:696px;height:81px"></div>
<h2 class="abs side-title" style="left:651px;top:702px">Hours</h2>
<div class="abs dotted" style="left:648px;top:729px;width:203px"></div>
<div class="abs hours-row" style="top:733px"><b>Mon To Thu</b> - 9:00am - 8:00pm</div>
<div class="abs hours-row" style="top:755px"><b>Saturday</b> - 9:00am - 3:00pm</div>

<!-- Blog -->
<h2 class="abs section-title" style="left:135px;top:798px">Recent Blog <em>Posts</em></h2>
<div class="abs blog-arrow" style="left:819px;top:804px"></div>
<svg class="abs" style="left:823px;top:808px" width="8" height="8" viewBox="0 0 8 8"><path d="M5 1L2 4l3 3" fill="none" stroke="#333" stroke-width="1.3"/></svg>
<div class="abs blog-arrow" style="left:841px;top:804px;border-color:var(--blue)"></div>
<svg class="abs" style="left:845px;top:808px" width="8" height="8" viewBox="0 0 8 8"><path d="M3 1l3 3-3 3" fill="none" stroke="#2e74b5" stroke-width="1.3"/></svg>
<div class="abs dotted" style="left:135px;top:827px;width:725px"></div>

<div class="abs avatar" style="left:133px;top:842px" role="img" aria-label="Portrait photo of the post author"></div>
<div class="abs blog-author" style="left:132px;top:908px">Lorem ipsum</div>
<div class="abs blog-head" style="left:217px;top:846px"><span>Lorem ipsum</span><span>09th OCT, 2014</span></div>
<p class="abs blog-text" style="left:217px;top:868px">sed dia nonumi consect uerol adipiscing sed diaer nonum nibh consel The uerol adipiscing elit ueroli adipiscing sederewr.</p>
<div class="abs col-divider" style="left:495px;top:845px;height:80px;border-left:1px solid #ddd"></div>
<div class="abs avatar" style="left:522px;top:842px" role="img" aria-label="Portrait photo of the post author"></div>
<div class="abs blog-author" style="left:522px;top:908px">Lorem ipsum</div>
<div class="abs blog-head" style="left:607px;top:846px;width:250px"><span>Lorem ipsum</span><span>08th OCT, 2014</span></div>
<p class="abs blog-text" style="left:607px;top:868px">sed dia nonumi consect uerol adipiscing sed diaer nonum nibh consel The uerol adipiscing elit ueroli adipiscing sederewr.</p>

<!-- Footer -->
<svg class="abs footer-shape" viewBox="0 0 991 310">
  <defs>
    <linearGradient id="footGrad" x1="0" y1="0" x2="1" y2="0">
      <stop offset="0" stop-color="#d05a0c"/>
      <stop offset=".5" stop-color="#efbd8f"/>
      <stop offset="1" stop-color="#d05a0c"/>
    </linearGradient>
  </defs>
  <path d="M0 70C180 130 430 120 720 45C830 25 920 22 991 25V310H0Z" fill="url(#footGrad)"/>
  <path d="M0 10C150 95 420 120 720 45C450 110 180 120 0 60Z" fill="#12387f"/>
</svg>

<h3 class="abs foot-title" style="left:110px">Quick Links</h3>
<div class="abs foot-rule" style="left:110px;top:1051px;width:103px"></div>
<ul class="abs quick-links">
  <li>Home</li>
  <li>Accredited Exercise Physiologist</li>
  <li>Services</li>
  <li>Contact</li>
</ul>
<div class="abs foot-divider" style="left:248px"></div>

<h3 class="abs foot-title" style="left:271px">Contact Details</h3>
<div class="abs foot-rule" style="left:271px;top:1051px;width:344px"></div>
<div class="abs foot-contact" style="top:1062px">
  <svg width="12" height="15" viewBox="0 0 14 18"><path d="M7 0a7 7 0 0 1 7 7c0 5-7 11-7 11S0 12 0 7a7 7 0 0 1 7-7z" fill="#fff"/><circle cx="7" cy="7" r="2.5" fill="#e29a5c"/></svg>
  <span>Street Name, City Name,<br>State, Pin Code</span>
</div>
<div class="abs foot-contact strong" style="top:1099px">
  <svg width="12" height="12" viewBox="0 0 20 20"><path d="M4 1l4 4-2 3 6 6 3-2 4 4-3 3C8 19 1 12 1 4z" fill="#fff"/></svg>
  <span>123-456-7890</span>
</div>
<div class="abs foot-contact strong" style="top:1120px">
  <svg width="12" height="14" viewBox="0 0 10 14"><rect x="1" y="0" width="8" height="14" rx="1.5" fill="#fff"/><rect x="2.5" y="2" width="5" height="8" fill="#e29a5c"/></svg>
  <span>456-789-1234</span>
</div>
<div class="abs foot-contact" style="top:1142px">
  <svg width="14" height="10" viewBox="0 0 16 12"><rect x="0" y="1" width="16" height="10" fill="#fff"/><path d="M0 1l8 6 8-6" fill="none" stroke="#e29a5c"/></svg>
  <span>info@brightstride.com</span>
</div>
<div class="abs foot-map" role="img" aria-label="City map showing the clinic area"></div>
<div class="abs foot-divider" style="left:645px"></div>

<h3 class="abs foot-title" style="left:679px">Subscribe for Newsletter</h3>
<div class="abs foot-rule" style="left:679px;top:1051px;width:201px"></div>
<p class="abs newsletter-copy">Lorem ipsum dolor sit a conur ut adiisci dolor sit a constetur ut adiisci</p>
<div class="abs email-field">Enter your email</div>
<div class="abs subscribe">SUBSCRIBE</div>
<div class="abs follow">Follow Us On :</div>
<div class="abs social" style="left:762px;background:#2f5aa8"></div>
<div class="abs social" style="left:794px;background:#2fa8e0"></div>
<div class="abs social" style="left:826px;background:#1d6fb0"></div>
<div class="abs social" style="left:858px;background:#f19a1c"></div>

<p class="abs copyright">Copyright 2014 Brightstride.&nbsp; All Rights Reserved</p>

</body>
</html>
```